Company Website for an IT business called "BRIGHT CORRIDOR"

Complete website creation with text and graphics.
We need :
- modern and creative design for our IT company
- Content management system to edit text later on
- Integrate third party content from partner company
- Contact form (transfer by email)
Updates

Designs look the same

Target Market(s)

Small and medium business
private customers

Industry/Entity Type

Information Technology

Coding

Coded - Design and coding required

Number of Pages Required

1 page

Font styles to use
Sans Serif

Requirements
Must have
• Contact form
Link to legal information
Link to data protection (GDPR)
Link to website owner declaration
Nice to have
• Fresh and creative graphics for IT business

```html
<!DOCTYPE html>
<html lang="en">
<head>
<meta charset="utf-8">
<title>Bright Corridor – IT Services</title>
<link rel="stylesheet" href="https://fonts.googleapis.com/css2?family=Poppins:wght@300;400;500;600;700;800&display=swap">
<style>
:root{
  --navy:#14134a;
  --navy-deep:#0c0b33;
  --blue:#0b9ddc;
  --blue-dark:#0a86c4;
  --ink:#2b2b2f;
  --text:#5c5c63;
  --muted:#9a9aa3;
  --dark:#1c1d21;
  --card:#29292c;
  --card-line:#3a3a3e;
  --light:#f4f4f5;
  --white:#ffffff;
}
*{box-sizing:border-box;margin:0;padding:0}
html,body{width:1200px;height:4101px;overflow:hidden}
body{font-family:"Poppins",sans-serif;background:var(--white);color:var(--ink);position:relative}
.abs{position:absolute}
.center{left:0;width:1200px;text-align:center}

/* header + hero */
.hero{position:absolute;left:0;top:0;width:1200px;height:836px;overflow:hidden}
.hero-bg{position:absolute;inset:0;background:
  radial-gradient(ellipse 700px 360px at 600px 560px,#1f54b8 0%,rgba(31,84,184,0) 70%),
  linear-gradient(180deg,var(--navy) 0%,#16236e 55%,#1a3e9c 100%)}
.hero-shape{position:absolute;left:0;top:0}
.brand{position:absolute;left:150px;top:40px;display:flex;align-items:center;gap:10px;color:var(--white);font-size:19px;font-weight:500;letter-spacing:2px}
.brand-dot{width:14px;height:14px;border-radius:50%;background:var(--blue)}
.nav{position:absolute;top:40px;left:500px;display:flex;gap:0;font-size:14px;color:#c9cbe6}
.nav a{position:absolute;white-space:nowrap;color:inherit;text-decoration:none}
.nav a.active{color:var(--white)}
.nav a.active::after{content:"";position:absolute;left:0;right:0;bottom:-6px;height:2px;background:var(--blue)}
.nav-cta{position:absolute;left:920px;top:32px;width:129px;height:38px;border:1.5px solid var(--blue);border-radius:19px;color:#c9cbe6;font-size:14px;display:flex;align-items:center;justify-content:center}
.hero-kicker{top:278px;font-size:20px;font-weight:400;color:var(--white)}
.hero-title{font-weight:800;color:var(--white);font-size:44px;line-height:1;letter-spacing:-1px}
.hero-title.l1{top:314px}
.hero-title.l2{top:366px}
.hero-rule{position:absolute;top:389px;height:2px;width:70px;background:rgba(255,255,255,.8)}
.btn{position:absolute;display:flex;align-items:center;justify-content:center;border-radius:21px;font-size:12px;font-weight:600;text-transform:uppercase}
.btn-blue{background:var(--blue);color:var(--white)}
.btn-white{background:var(--white);color:var(--navy)}
.hero-badge{position:absolute;left:564px;top:680px;width:72px;height:72px;border-radius:50%;background:var(--white);box-shadow:0 0 0 6px rgba(255,255,255,.35)}

/* about */
.eyebrow{left:150px;top:885px;color:var(--blue);font-size:20px;font-weight:400}
.about-title{left:150px;top:918px;font-size:26px;font-weight:700;line-height:40px;color:var(--ink)}
.about-copy{left:150px;top:1006px;width:450px;font-size:13px;line-height:24px;color:var(--text)}
.photo{position:absolute}
.photo-back{left:730px;top:866px;width:320px;height:312px;background:linear-gradient(135deg,#bfc1c4,#6b6e73 60%,#3e4044)}
.photo-front{left:664px;top:926px;width:305px;height:271px;background:linear-gradient(135deg,#8b8d91,#4c4e52 55%,#26272a)}
.photo-frame{position:absolute;left:705px;top:901px;width:290px;height:322px;border:5px solid var(--blue)}

/* provide */
.dark-band{position:absolute;left:0;top:1270px}
.section-title{font-size:32px;font-weight:400;line-height:1}
.section-title b{font-weight:700}
.title-rule{position:absolute;left:570px;width:60px;height:3px;background:var(--blue)}
.section-lead{width:540px;left:330px;font-size:14px;line-height:22px;text-align:center}
.card{position:absolute;width:283px;height:276px;background:var(--card);border:1px solid var(--card-line);text-align:center;color:var(--white)}
.card.is-featured{background:var(--blue-dark);border-color:var(--blue-dark)}
.card-icon{position:absolute;left:116px;top:22px}
.card-divider{position:absolute;left:40px;top:104px;width:203px;height:1px;background:linear-gradient(90deg,rgba(255,255,255,0),rgba(255,255,255,.5),rgba(255,255,255,0))}
.card-divider::after{content:"";position:absolute;left:98px;top:-3px;width:7px;height:7px;border-radius:50%;background:var(--white)}
.card-title{position:absolute;left:0;right:0;top:126px;font-size:15px;font-weight:600}
.card-copy{position:absolute;left:24px;right:24px;top:158px;font-size:12px;line-height:21px;color:#d6d6da}
.card-link{position:absolute;left:0;right:0;top:228px;font-size:12px;font-weight:500;color:var(--blue);text-decoration:underline}
.card.is-featured .card-link{color:var(--white)}
.card.is-featured .card-copy{color:#e8f5fc}

/* why */
.stat{position:absolute;top:2612px;width:182px;height:157px;background:#f3f5f8;text-align:center}
.stat::before{content:"";position:absolute;left:-7px;top:-7px;width:196px;height:171px;border-top:2px solid #7c8da3;border-left:2px solid #7c8da3}
.stat::after{content:"";position:absolute;left:-7px;top:-7px;width:196px;height:171px;border-bottom:2px solid #7c8da3;border-right:2px solid #7c8da3;transform:translate(14px,0)}
.stat-value{position:absolute;left:0;right:0;top:22px;font-size:24px;font-weight:700;color:var(--blue-dark)}
.stat-label{position:absolute;left:0;right:0;top:70px;font-size:14px;font-weight:600;color:var(--ink)}
.stat-note{position:absolute;left:28px;right:28px;top:96px;font-size:11px;line-height:18px;color:var(--text)}

/* contact */
.contact-zone{position:absolute;left:0;top:2841px;width:1200px;height:720px;background:var(--light)}
.contact-panel{position:absolute;left:150px;top:2928px;width:412px;height:357px;background:linear-gradient(135deg,#1aa6e4,#0b8fd0)}
.contact-panel h2{position:absolute;left:60px;top:112px;font-size:30px;font-weight:700;color:var(--white);line-height:1}
.contact-panel h2 span{font-weight:300}
.contact-panel .rule{position:absolute;left:60px;top:155px;width:36px;height:2px;background:var(--white)}
.contact-panel p{position:absolute;left:60px;top:170px;width:210px;font-size:11px;line-height:20px;color:#e6f5fc}
.form-card{position:absolute;left:477px;top:2976px;width:573px;height:451px;background:var(--white);box-shadow:0 12px 40px rgba(20,20,60,.08)}
.form-card h2{position:absolute;left:51px;top:62px;font-size:30px;font-weight:300;line-height:1;color:var(--ink)}
.form-card h2 b{font-weight:600}
.field{position:absolute;border-bottom:1px solid #d9d9de;height:44px}
.field label{position:absolute;left:2px;top:0;font-size:10px;font-weight:600;color:var(--ink);text-transform:uppercase}
.field span{position:absolute;left:2px;top:26px;font-size:10px;color:var(--muted)}
.send{position:absolute;width:60px;height:60px;border-radius:50%;background:var(--blue);box-shadow:0 6px 16px rgba(11,157,220,.4);display:flex;align-items:center;justify-content:center}

/* footer */
.footer-bg{position:absolute;left:0;top:3400px}
.news-title{top:3660px;font-size:20px;font-weight:700;color:var(--white)}
.news-sub{top:3693px;font-size:12px;color:#a8a8b0}
.news-input{position:absolute;left:336px;top:3727px;width:535px;height:42px;border-radius:21px;background:var(--white);font-size:11px;color:var(--muted);display:flex;align-items:center;padding-left:26px;gap:6px}
.news-send{position:absolute;right:5px;top:5px;width:32px;height:32px;border-radius:50%;background:var(--blue);display:flex;align-items:center;justify-content:center}
.footer-rule{position:absolute;left:150px;top:3804px;width:900px;height:1px;background:#34353a}
.footer-brand{position:absolute;left:0;width:1200px;top:3868px;display:flex;justify-content:center;align-items:center;gap:12px;color:var(--white);font-size:24px;font-weight:500;letter-spacing:3px}
.footer-nav a{position:absolute;top:3934px;font-size:14px;color:var(--white);text-decoration:none;white-space:nowrap}
.copyright{left:173px;top:4013px;font-size:12px;color:#d0d0d6}
.social{position:absolute;top:4007px;width:30px;height:30px;border-radius:50%;background:var(--blue)}
</style>
</head>
<body>

<!-- Hero -->
<header class="hero">
  <div class="hero-bg" role="img" aria-label="Deep blue digital city skyline with glowing data points rising into the sky"></div>
  <svg class="hero-shape" width="1200" height="836" viewBox="0 0 1200 836">
    <polygon points="0,775 1200,690 1200,836 0,836" fill="#ffffff"/>
    <polygon points="600,772 1200,665 1200,836" fill="#0b9ddc"/>
  </svg>
  <div class="brand"><span class="brand-dot"></span>BRIGHT CORRIDOR</div>
  <nav class="nav">
    <a class="active" style="left:0">Home</a>
    <a style="left:80px">About</a>
    <a style="left:165px">Services</a>
    <a style="left:262px">Data Protection</a>
  </nav>
  <div class="nav-cta">Contact Us</div>
  <p class="abs center hero-kicker">THE RIGHT PEOPLE FOR YOUR TEAM.</p>
  <h1 class="abs center hero-title l1">CONNECTING THE</h1>
  <p class="abs center hero-title l2">WORLD</p>
  <span class="hero-rule" style="left:432px"></span>
  <span class="hero-rule" style="left:698px"></span>
  <div class="btn btn-blue" style="left:462px;top:429px;width:132px;height:40px">Get Started</div>
  <div class="btn btn-white" style="left:606px;top:429px;width:132px;height:40px">Learn More</div>
  <div class="hero-badge"></div>
</header>

<!-- About -->
<section>
  <p class="abs eyebrow">About Us</p>
  <h2 class="abs about-title">LOREM IPSUM IS SIMPLY DUMMY<br>TEXT OF THE PRINTING</h2>
  <p class="abs about-copy">Lorem Ipsum is simply dummy text of the printing and typesetting industry. Lorem Ipsum has been the industry's standard dummy text ever since the 1500s, when an unknown printer took a galley of type and scrambled it to make a type specimen book. It has survived not only five centuries, but also the leap into electronic typesetting, remaining essentially unchanged.</p>
  <div class="btn btn-blue" style="left:150px;top:1177px;width:159px;height:40px">More About Us</div>
  <div class="photo photo-back" role="img" aria-label="Black and white photo of colleagues working at computers"></div>
  <div class="photo photo-front" role="img" aria-label="Photo of two coworkers discussing work at a desktop computer"></div>
  <div class="photo-frame"></div>
</section>

<!-- Services -->
<section>
  <svg class="dark-band" width="1200" height="1170" viewBox="0 0 1200 1170">
    <polygon points="0,186 1200,76 1200,1057 0,1165" fill="#1c1d21"/>
    <polygon points="0,11 541,130 0,186" fill="#0b9ddc"/>
  </svg>
  <h2 class="abs center section-title" style="top:1494px;color:#fff">WHAT <b>WE PROVIDE</b></h2>
  <span class="title-rule" style="top:1539px"></span>
  <p class="abs section-lead" style="top:1565px;color:#e0e0e4">Lorem Ipsum is simply dummy text of the printing and typesetting industry. Lorem Ipsum has been the industry's standard dummy text .</p>

  <article class="card" style="left:150px;top:1647px">
    <svg class="card-icon" width="52" height="60" viewBox="0 0 52 60" fill="none" stroke="#fff" stroke-width="1.6"><path d="M26 22 C14 12 10 4 18 3 C22 3 25 6 26 8 C27 6 30 3 34 3 C42 4 38 12 26 22Z"/><circle cx="10" cy="38" r="4"/><circle cx="26" cy="38" r="4"/><circle cx="42" cy="38" r="4"/><path d="M3 54 C3 46 17 46 17 54Z M19 54 C19 46 33 46 33 54Z M35 54 C35 46 49 46 49 54Z M26 22 V32"/></svg>
    <span class="card-divider"></span>
    <h3 class="card-title">CUSTOMER SATISFACTION</h3>
    <p class="card-copy">Lorem Ipsum is simply dummy text of the printing and typesetting industry. Lorem Ipsum has been.</p>
    <span class="card-link">LEARN MORE</span>
  </article>
  <article class="card is-featured" style="left:458px;top:1647px">
    <svg class="card-icon" width="52" height="60" viewBox="0 0 52 60" fill="none" stroke="#fff" stroke-width="1.6"><path d="M16 18 a8 8 0 0 1 8-10 a9 9 0 0 1 16 4 a6 6 0 0 1 0 12 H18 a6 6 0 0 1-2-6Z"/><rect x="22" y="26" width="10" height="8"/><path d="M24 26 v-3 a3 3 0 0 1 6 0 v3 M4 38 h10 v16 h-10Z M14 50 C26 56 34 54 46 44 C44 40 40 42 36 44 L28 46"/></svg>
    <span class="card-divider"></span>
    <h3 class="card-title">DATA PROTECTION</h3>
    <p class="card-copy">Lorem Ipsum is simply dummy text of the printing and typesetting industry. Lorem Ipsum has been.</p>
    <span class="card-link">LEARN MORE</span>
  </article>
  <article class="card" style="left:767px;top:1647px">
    <svg class="card-icon" width="52" height="60" viewBox="0 0 52 60" fill="none" stroke="#fff" stroke-width="1.6"><rect x="16" y="4" width="20" height="14"/><rect x="2" y="18" width="48" height="12"/><path d="M8 30 v22 M44 30 v22 M18 30 v14 h16 v-14 M22 44 v10 M30 44 v10"/></svg>
    <span class="card-divider"></span>
    <h3 class="card-title">IT CONSULTING</h3>
    <p class="card-copy">Lorem Ipsum is simply dummy text of the printing and typesetting industry. Lorem Ipsum has been.</p>
    <span class="card-link">LEARN MORE</span>
  </article>
  <article class="card" style="left:150px;top:1950px">
    <svg class="card-icon" width="52" height="60" viewBox="0 0 52 60" fill="none" stroke="#fff" stroke-width="1.6"><rect x="8" y="2" width="36" height="48" rx="3"/><path d="M26 10 v18 M16 14 h20 M16 14 l-4 10 h8Z M36 14 l-4 10 h8Z M18 30 h16 M14 38 h24"/><path d="M20 50 v8 l6-4 6 4 v-8"/></svg>
    <span class="card-divider"></span>
    <h3 class="card-title">LEGAL INFORMATION</h3>
    <p class="card-copy">Lorem Ipsum is simply dummy text of the printing and typesetting industry. Lorem Ipsum has been.</p>
    <span class="card-link">LEARN MORE</span>
  </article>
  <article class="card" style="left:458px;top:1950px">
    <svg class="card-icon" width="52" height="60" viewBox="0 0 52 60" fill="none" stroke="#fff" stroke-width="1.6"><rect x="10" y="6" width="32" height="46" rx="2"/><path d="M6 6 h40 M6 52 h24 M16 16 h20 M16 22 h20 M16 28 h20 M16 34 h12"/><circle cx="38" cy="46" r="6"/><path d="M35 52 v6 l3-2 3 2 v-6"/></svg>
    <span class="card-divider"></span>
    <h3 class="card-title">DECLARATION</h3>
    <p class="card-copy">Lorem Ipsum is simply dummy text of the printing and typesetting industry. Lorem Ipsum has been.</p>
    <span class="card-link">LEARN MORE</span>
  </article>
  <article class="card" style="left:767px;top:1950px">
    <svg class="card-icon" width="52" height="60" viewBox="0 0 52 60" fill="none" stroke="#fff" stroke-width="1.6"><circle cx="28" cy="20" r="14"/><circle cx="28" cy="20" r="6"/><path d="M28 2 v4 M28 34 v4 M10 20 h4 M42 20 h4 M4 42 h8 v14 h-8Z M12 44 h12 c4 0 4 6 0 6 h-6 M12 54 C26 58 38 54 48 42 C46 38 42 40 38 44"/></svg>
    <span class="card-divider"></span>
    <h3 class="card-title">IT SUPPORT</h3>
    <p class="card-copy">Lorem Ipsum is simply dummy text of the printing and typesetting industry. Lorem Ipsum has been.</p>
    <span class="card-link">LEARN MORE</span>
  </article>
</section>

<!-- Why choose us -->
<section>
  <h2 class="abs center section-title" style="top:2456px;color:var(--ink)">WHY <b>CHOSE US</b></h2>
  <span class="title-rule" style="top:2506px"></span>
  <p class="abs section-lead" style="top:2526px;color:var(--text);font-size:13px">Lorem Ipsum is simply dummy text of the printing and typesetting industry. Lorem Ipsum has been the industry's standard dummy text .</p>
  <div class="stat" style="left:235px"><p class="stat-value">24 / 7/ 365</p><p class="stat-label">SUPPORT</p><p class="stat-note">Our experts are always on the job for you</p></div>
  <div class="stat" style="left:509px"><p class="stat-value">20 YEARS</p><p class="stat-label">EXPERTISE</p><p class="stat-note">Our experts are always on the job for you</p></div>
  <div class="stat" style="left:784px"><p class="stat-value">UP TO 50%</p><p class="stat-label">SAVINGS</p><p class="stat-note">Our experts are always on the job for you</p></div>
</section>

<!-- Contact -->
<section>
  <div class="contact-zone"></div>
  <div class="contact-panel" role="img" aria-label="Blue-tinted photo of a team meeting in an office">
    <h2>CONTACT <span>US</span></h2>
    <span class="rule"></span>
    <p>Lorem ipsum dolor amet, consectetur adipiscing elit curabitur imperdiet pharetra vestibulum morbi maximus molestie magna amet.</p>
  </div>
  <form class="form-card">
    <h2>GET IN <b>TOUCH</b></h2>
    <div class="field" style="left:53px;top:135px;width:207px"><label>First Name</label><span>Daniel</span></div>
    <div class="field" style="left:308px;top:135px;width:210px"><label>Last Name</label><span>Reed</span></div>
    <div class="field" style="left:53px;top:220px;width:207px"><label>Email Address</label><span>danielreed@mailhub.net</span></div>
    <div class="field" style="left:308px;top:220px;width:210px"><label>Phone</label><span>555-210-4836</span></div>
    <div class="field" style="left:53px;top:307px;width:425px;height:70px"><label>Message</label><span>Hi, do you have a moment to talk abo...|</span></div>
    <div class="send" style="left:459px;top:325px">
      <svg width="22" height="22" viewBox="0 0 24 24"><path d="M2 11 L22 2 L15 22 L11 13Z" fill="#fff"/></svg>
    </div>
  </form>
</section>

<!-- Footer -->
<footer>
  <svg class="footer-bg" width="1200" height="701" viewBox="0 0 1200 701">
    <polygon points="0,125 1200,50 1200,701 0,701" fill="#1c1d21"/>
    <polygon points="652,184 1200,55 1200,120" fill="#0b9ddc"/>
  </svg>
  <h2 class="abs center news-title">SUBSCRIBE NEWSLETTER</h2>
  <p class="abs center news-sub">Lorem ipsum dolor amet, consectetur adipiscing elit tempor</p>
  <div class="news-input">
    <svg width="12" height="10" viewBox="0 0 12 10" fill="none" stroke="#9a9aa3"><rect x="0.5" y="0.5" width="11" height="9" rx="1"/><path d="M1 1 L6 5 L11 1"/></svg>
    Email Address
    <span class="news-send"><svg width="14" height="14" viewBox="0 0 24 24"><path d="M2 11 L22 2 L15 22 L11 13Z" fill="#fff"/></svg></span>
  </div>
  <span class="footer-rule"></span>
  <div class="footer-brand"><span class="brand-dot"></span>BRIGHT CORRIDOR</div>
  <nav class="footer-nav">
    <a style="left:339px">Home</a>
    <a style="left:419px">About</a>
    <a style="left:504px">Services</a>
    <a style="left:601px">Data Protection</a>
    <a style="left:779px">Contact Us</a>
  </nav>
  <p class="abs copyright">© 2021 Bright Corridor. All Rights Reserved.</p>
  <span class="social" style="left:836px"></span>
  <span class="social" style="left:871px"></span>
  <span class="social" style="left:906px"></span>
  <span class="social" style="left:945px"></span>
</footer>

</body>
</html>
```